Billboard design for a jewelry store.

I am looking for a very unique design with a catchy slogan, I am looking for billboard so good that will make the front page of the newspaper. I want to target customers that are looking for diamond jewelry or diamonds in general. For sure not interested in anything that is genetic or been used in the past. I want the billboard to stand out and very unique. Text not more than 3 words, our logo and an image.

Target Market(s)

Local

Industry/Entity Type

Jewelry Store

Font styles to use
Other font styles liked:
• Open to your suggestion for the font.

Requirements
Must have
• Unique, very brief a catchy slogan. My logo and an image. Open for suggestions. I want also different formats to use on social media.
Nice to have
• I am open to unique and amazing new ideas. I don't want general used design or slogan.
Should not have
• Too much text

```html
<!DOCTYPE html>
<html lang="en">
<head>
<meta charset="utf-8">
<title>Velari Jewelers – Bring a Sparkle Billboard</title>
<link rel="stylesheet" href="https://fonts.googleapis.com/css2?family=Cinzel:wght@400;700&family=Cormorant+Garamond:wght@500&display=swap">
<style>
  :root {
    --stage: #c9c9c9;
    --stage-light: #e4e4e4;
    --board: #050505;
    --ink: #ffffff;
    --ink-soft: #e8e8e8;
    --gold: #8a6a2e;
    --stone: #cfd6e0;
  }
  html, body {
    margin: 0;
    padding: 0;
    width: 1120px;
    height: 1200px;
    overflow: hidden;
  }
  body {
    background: radial-gradient(ellipse at 50% 40%, var(--stage-light), var(--stage) 75%);
    position: relative;
  }
  .billboard {
    position: absolute;
    left: 80px;
    top: 408px;
    width: 960px;
    height: 384px;
    background: var(--board);
    overflow: hidden;
    box-shadow: 0 6px 18px rgba(0,0,0,0.35);
  }
  .billboard__ambient {
    position: absolute;
    inset: 0;
    background:
      radial-gradient(circle at 30% 70%, rgba(120,90,60,0.18), transparent 40%),
      radial-gradient(circle at 45% 45%, rgba(60,80,90,0.15), transparent 35%);
  }
  .billboard__photo {
    position: absolute;
    top: 0;
    right: 0;
    width: 330px;
    height: 100%;
    background:
      radial-gradient(circle at 52% 46%, var(--stone) 0, #8f98a6 9%, transparent 17%),
      radial-gradient(ellipse at 55% 50%, rgba(180,140,70,0.75), rgba(90,65,25,0.4) 38%, transparent 62%),
      linear-gradient(90deg, var(--board), #1a140b 40%, #0c0a07);
  }
  .billboard__frame {
    position: absolute;
    left: 15px;
    top: 17px;
    right: 15px;
    bottom: 17px;
    border: 1px solid var(--ink-soft);
    pointer-events: none;
  }
  .brand {
    position: absolute;
    left: 190px;
    top: 40px;
    width: 270px;
    text-align: center;
    color: var(--ink);
    font-family: "Cinzel", serif;
    font-weight: 700;
  }
  .brand__name {
    display: block;
    font-size: 56px;
    line-height: 1;
    letter-spacing: 2px;
  }
  .brand__trade {
    display: block;
    font-size: 16px;
    letter-spacing: 9px;
    margin-top: 2px;
  }
  .slogan {
    position: absolute;
    left: 34px;
    top: 186px;
    margin: 0;
    color: var(--ink);
    font-family: "Cinzel", serif;
    font-weight: 400;
    font-size: 66px;
    line-height: 1;
    letter-spacing: 1px;
    white-space: nowrap;
  }
  .web {
    position: absolute;
    left: 190px;
    top: 326px;
    width: 270px;
    text-align: center;
    color: var(--ink);
    font-family: "Cormorant Garamond", serif;
    font-weight: 500;
    font-size: 19px;
  }
</style>
</head>
<body>
  <section class="billboard" aria-label="Velari Jewelers billboard">
    <div class="billboard__ambient"></div>
    <div class="billboard__photo" role="img" aria-label="Close-up photo of a gold ring with a large sparkling diamond on a dark background"></div>
    <div class="billboard__frame"></div>
    <div class="brand">
      <span class="brand__name">VELARI</span>
      <span class="brand__trade">JEWELERS</span>
    </div>
    <h1 class="slogan">Bring a Sparkle</h1>
    <div class="web">www.velarijewelers.com</div>
  </section>
</body>
</html>
```